Alberta, Canada based Environmental Oilfield Consultant need a Business Card Design

We need a business card design for a year old company based in Edmonton, Alberta, Canada called Brambleton Consulting Inc. We are environmental consultants primarily for oilfield based companies (pipeline cleanup, site consultations, environmental site training, and site evaluations).

We like the color blue or green, something very clean and crisp looking.
We don't really care if there is an otter on it but most of our work is land based and nothing really to do with oceans or larger bodies of water.

The name Brambleton was the name of our fathers boat, and named our company that in his memory.

```html
<!DOCTYPE html>
<html lang="en">
<head>
<meta charset="utf-8">
<title>Brambleton Consulting Inc. – Business Card</title>
<link href="https://fonts.googleapis.com/css2?family=Arimo:wght@400;700&display=swap" rel="stylesheet">
<style>
  :root {
    --green: #10ad72;
    --grey-light: #ededed;
    --grey-mid: #cfcfcf;
    --grey-dark: #b4b4b4;
    --text-grey: #8a8a8a;
    --white: #ffffff;
    --backdrop: #e4e2de;
  }
  * { box-sizing: border-box; margin: 0; padding: 0; }
  html, body { width: 1200px; height: 900px; overflow: hidden; }
  body {
    background: var(--backdrop);
    font-family: "Arimo", Arial, sans-serif;
    display: flex;
    flex-direction: column;
    align-items: center;
    justify-content: center;
    gap: 56px;
  }
  .card {
    position: relative;
    width: 620px;
    height: 354px;
    overflow: hidden;
    background: radial-gradient(ellipse at 55% 40%, var(--grey-light) 0%, var(--grey-mid) 75%, var(--grey-dark) 100%);
    box-shadow: 0 6px 18px rgba(0,0,0,0.18);
  }
  .card-shapes { position: absolute; inset: 0; }

  /* Contact side */
  .person { position: absolute; right: 150px; top: 58px; text-align: right; color: var(--green); }
  .person-name { font-size: 34px; font-weight: 400; }
  .person-role { font-size: 14px; font-style: italic; margin-top: 4px; }
  .contact { position: absolute; left: 34px; top: 150px; color: var(--text-grey); font-size: 14px; line-height: 1.7; }
  .contact-phones { display: flex; align-items: center; gap: 10px; }
  .contact-phones .divider { width: 1px; height: 20px; background: var(--text-grey); }
  .contact-item { display: inline-flex; align-items: center; gap: 6px; }
  .contact-item svg { width: 14px; height: 14px; fill: var(--text-grey); }
  .band-brand {
    position: absolute; right: 32px; bottom: 34px;
    color: var(--white); font-size: 30px; font-weight: 700;
  }

  /* Company side */
  .brand {
    position: absolute; left: 0; right: 0; top: 38px;
    text-align: center; color: var(--green); font-weight: 700; line-height: 1;
  }
  .brand-name { display: block; font-size: 68px; letter-spacing: -1px; }
  .brand-suffix { display: block; font-size: 22px; letter-spacing: 3px; text-transform: uppercase; margin-top: 12px; }
  .services {
    position: absolute; left: 0; right: 0; top: 178px; height: 64px;
    background: var(--white);
    color: var(--green); font-size: 16px; text-align: center; line-height: 1.35;
    display: flex; align-items: center; justify-content: center;
  }
  .region {
    position: absolute; left: 0; right: 0; top: 242px; height: 24px;
    background: var(--grey-dark);
    color: var(--white); font-size: 12px; letter-spacing: 22px; text-align: center; line-height: 24px;
    padding-left: 22px;
  }
  .website {
    position: absolute; left: 0; right: 0; top: 292px;
    color: var(--green); font-size: 17px; letter-spacing: 4px; text-align: center;
    padding-left: 4px;
  }
</style>
</head>
<body>

  <section class="card card-contact">
    <svg class="card-shapes" viewBox="0 0 620 354" aria-hidden="true">
      <polygon points="170,0 310,0 170,70" fill="var(--green)"/>
      <polygon points="250,354 620,354 620,240 360,240" fill="var(--green)"/>
    </svg>
    <div class="person">
      <p class="person-name">Dana Mercer</p>
      <p class="person-role">Designation</p>
    </div>
    <div class="contact">
      <div class="contact-phones">
        <span class="contact-item">
          <svg viewBox="0 0 24 24"><path d="M6.6 10.8a15 15 0 0 0 6.6 6.6l2.2-2.2a1 1 0 0 1 1-.25 11.4 11.4 0 0 0 3.6.57 1 1 0 0 1 1 1V20a1 1 0 0 1-1 1A17 17 0 0 1 3 4a1 1 0 0 1 1-1h3.5a1 1 0 0 1 1 1c0 1.250.2 2.450.57 3.570a1 1 0 0 1-.25 1z"/></svg>
          780-555-0132
        </span>
        <span class="divider"></span>
        <span class="contact-item">
          <svg viewBox="0 0 24 24"><path d="M7 1h10a2 2 0 0 1 2 2v18a2 2 0 0 1-2 2H7a2 2 0 0 1-2-2V3a2 2 0 0 1 2-2zm0 3v15h10V4z"/></svg>
          780-555-0178
        </span>
      </div>
      <p>email: dana@brambleton.co</p>
      <p>addres: street-12 larkfield abt.</p>
    </div>
    <p class="band-brand">Brambleton</p>
  </section>

  <section class="card card-company">
    <h1 class="brand">
      <span class="brand-name">Brambleton</span>
      <span class="brand-suffix">Consulting Inc.</span>
    </h1>
    <p class="services">Pipeline Cleanup, Site Consultations, Environmental<br>Site Training, And Site Evaluations</p>
    <p class="region">ALBARTA CANADA</p>
    <p class="website">www.brambleton.com</p>
  </section>

</body>
</html>
```